Gymnastics equipment catalogue

I have up to 4 pages to fill with gymnastics, sensory and flexible learning space equipment pictures and info. This will go in a 300 page sporting goods catalogue.
I would like the types of equipment separated into categories. I will need to give you additional pics and info. Too tricky to upload some of the pics.
I have an example that will show exactly what I want, but it won't upload. Happy to swap emails

Target Market(s)

School phys ed and special needs teachers

Industry/Entity Type

Sporting Good

Font styles to use
Sans Serif

Colors
3176b5
34a6d7
33b8a4
acd036
fbee3d
9bcb3c
876aae
e667a6

Requirements
Must have
• Pictures and prices and some info.
• I have alot more pictures and info. Finding it tricky to upload them. can email

```html
<!DOCTYPE html>
<html lang="en">
<head>
<meta charset="utf-8">
<title>Gymnastics Equipment Catalogue</title>
<link rel="stylesheet" href="https://fonts.googleapis.com/css2?family=Oswald:wght@300;600&family=Montserrat:wght@400;600;700&display=swap">
<style>
:root{
  --blue:#3176b5;
  --sky:#34a6d7;
  --teal:#33b8a4;
  --lime:#acd036;
  --green:#9bcb3c;
  --ink:#222;
  --grey:#8a8a8a;
  --paper:#ffffff;
  --row:#eeeeee;
  --stage:#e4e4e4;
}
*{box-sizing:border-box;margin:0;padding:0}
html,body{width:724px;height:1200px;overflow:hidden;background:var(--stage);font-family:"Montserrat",sans-serif;color:var(--ink)}
.canvas{position:relative;width:724px;height:1200px}
.cover{position:absolute;left:162px;top:28px;width:400px;height:566px;background:var(--paper);box-shadow:0 4px 14px rgba(0,0,0,.18);overflow:hidden}
.cover svg{position:absolute;inset:0}
.cover .brand{position:absolute;right:46px;top:54px;font-family:"Montserrat",sans-serif;font-weight:700;font-size:40px;letter-spacing:1px;color:var(--ink)}
.cover .title{position:absolute;left:188px;top:300px;line-height:1}
.cover .title .main{display:block;font-family:"Oswald",sans-serif;font-weight:600;font-size:40px;color:var(--teal);letter-spacing:.5px}
.cover .title .sub{display:block;font-family:"Oswald",sans-serif;font-weight:300;font-size:21px;color:var(--ink);letter-spacing:.3px;margin-top:2px}

.spread{position:absolute;left:22px;top:632px;width:680px;height:480px;display:flex;box-shadow:0 4px 14px rgba(0,0,0,.18)}
.page{position:relative;width:340px;height:480px;background:var(--paper);overflow:hidden}
.page.left{background:linear-gradient(90deg,#fff 80%,#e9e9e9)}
.page.right{background:linear-gradient(90deg,#e6e6e6,#fff 14%)}
.section-tab{position:absolute;left:0;top:38px;height:34px;width:190px;background:var(--blue);color:#fff;font-weight:700;font-size:14px;line-height:34px;padding-left:16px;letter-spacing:.3px}
.section-tab svg{position:absolute;right:-40px;top:3px}
.price-tables{position:absolute;left:18px;top:92px;width:300px}
.price-table{width:100%;border-collapse:separate;border-spacing:0 2px;font-size:6.5px;margin-bottom:8px}
.price-table th{background:var(--teal);color:#fff;font-weight:700;text-align:left;padding:4px 6px;font-size:7px}
.price-table th:first-child{border-radius:8px 0 0 0}
.price-table th:last-child{border-radius:0 8px 0 0}
.price-table th.num,.price-table td.num{width:58px;text-align:right}
.price-table td{background:var(--row);padding:3px 6px;color:#333}
.page-foot{position:absolute;left:0;right:0;bottom:0;height:18px;background:var(--teal)}
.page-foot .site{position:absolute;right:16px;top:4px;color:#fff;font-size:7px;font-weight:600}
.products{position:absolute;left:22px;top:28px;right:18px}
.product{display:flex;align-items:center;gap:12px;height:72px;margin-bottom:10px}
.product .shot{width:98px;height:68px;border-radius:8px;background:#fff;box-shadow:0 1px 5px rgba(0,0,0,.18);display:flex;align-items:center;justify-content:center}
.product .shot span{display:block;width:70px;height:40px;border-radius:4px}
.product p{flex:1;font-size:6.5px;line-height:1.45;color:var(--grey)}
</style>
</head>
<body>
<main class="canvas">

  <section class="cover">
    <svg width="400" height="566" viewBox="0 0 400 566">
      <g fill="#e3f4f1" opacity=".8">
        <rect x="230" y="0" width="80" height="80"/><rect x="300" y="20" width="60" height="60"/>
        <rect x="180" y="130" width="70" height="70" fill="#f1f1f1"/><rect x="260" y="170" width="60" height="60" fill="#f3f3f3"/>
        <rect x="330" y="120" width="70" height="70" fill="#eef6e0"/><rect x="220" y="240" width="50" height="50" fill="#f0f0f0"/>
      </g>
      <polygon points="0,330 120,330 0,450" fill="#2f6fb0" opacity=".9"/>
      <polygon points="0,350 210,350 60,470" fill="var(--blue)"/>
      <polygon points="150,350 250,350 210,470" fill="#a6d64a" opacity=".8"/>
      <polygon points="60,470 210,470 150,350" fill="var(--lime)" opacity=".9"/>
      <rect x="130" y="130" width="50" height="40" fill="var(--teal)"/>
      <g role="img" aria-label="Photo of a child using a laptop on soft play mats">
        <rect x="0" y="150" width="120" height="170" fill="#c9a24a"/>
      </g>
      <g role="img" aria-label="Photo of a young girl standing on a blue gymnastics mat">
        <rect x="130" y="160" width="150" height="170" fill="#2a5fb8"/>
      </g>
      <polygon points="0,566 400,566 400,470 120,520" fill="var(--teal)"/>
      <g role="img" aria-label="Product photo of a black mini trampoline">
        <ellipse cx="220" cy="430" rx="60" ry="30" fill="#2b2f33"/>
      </g>
      <g role="img" aria-label="Product photo of colourful foam shape blocks">
        <rect x="290" y="400" width="40" height="34" fill="#e05a3a"/>
        <rect x="338" y="392" width="44" height="36" fill="#3a8fd0"/>
      </g>
    </svg>
    <div class="brand">LOGO</div>
    <h1 class="title"><span class="main">GYMNASTICS</span><span class="sub">EQUIPMENT CATALOGUE</span></h1>
  </section>

  <section class="spread">
    <article class="page left">
      <h2 class="section-tab">ITEMS AND PRICES
        <svg width="40" height="28" viewBox="0 0 40 28"><g fill="none" stroke="var(--blue)" stroke-width="4"><path d="M4 4l10 10-10 10"/><path d="M16 4l10 10-10 10"/><path d="M28 4l10 10-10 10"/></g></svg>
      </h2>
      <div class="price-tables">
        <table class="price-table">
          <tr><th>ITEMS</th><th class="num">RRP</th><th class="num">WHOLESALE</th></tr>
          <tr><td>Mini tramp (folding light weight)</td><td class="num">$549.00</td><td class="num">$450.00</td></tr>
          <tr><td>Replacement bed and mat set with springs</td><td class="num">$270.00</td><td class="num">$220.00</td></tr>
          <tr><td>32 springs</td><td class="num">$192.00</td><td class="num">$120.00</td></tr>
        </table>
        <table class="price-table">
          <tr><th>FLOORING</th><th class="num">RRP</th><th class="num">WHOLESALE</th></tr>
          <tr><td>13000 x 2000 x 32mm</td><td class="num">$2,205.00</td><td class="num">$1,805.00</td></tr>
        </table>
        <table class="price-table">
          <tr><th>ITEMS</th><th class="num">RRP</th><th class="num">WHOLESALE</th></tr>
          <tr><td>Vault box</td><td class="num">$1,592.00</td><td class="num">$1,305.00</td></tr>
        </table>
        <table class="price-table">
          <tr><th>ITEMS</th><th class="num">RRP</th><th class="num">WHOLESALE</th></tr>
          <tr><td>Spring board</td><td class="num">$430.00</td><td class="num">$390.00</td></tr>
          <tr><td>Low beam</td><td class="num">$1,120.00</td><td class="num">$990.00</td></tr>
          <tr><td>Foam beam</td><td class="num">$480.00</td><td class="num">$340.00</td></tr>
          <tr><td>Folding wedge</td><td class="num">$1,200.00</td><td class="num">$990.00</td></tr>
          <tr><td>Crash mat</td><td class="num">$590.00</td><td class="num">$410.00</td></tr>
          <tr><td>Spotting box</td><td class="num">$292.00</td><td class="num">$205.00</td></tr>
          <tr><td>Wiggle stool</td><td class="num">$98.00</td><td class="num">$78.00</td></tr>
          <tr><td>Split legs</td><td class="num">$192.00</td><td class="num">$160.00</td></tr>
          <tr><td>Polyurea kids furniture</td><td class="num">$197.00</td><td class="num">$120.00</td></tr>
        </table>
      </div>
      <div class="page-foot"></div>
    </article>

    <article class="page right">
      <div class="products">
        <div class="product"><div class="shot" role="img" aria-label="Product photo of green foam balance pieces"><span style="background:#7cc142"></span></div><p>Lorem ipsum dolor sit amet, consectetur adipiscing elit. Aliquam rhoncus nulla sapien, tincidunt iaculis erat feugiat et.</p></div>
        <div class="product"><div class="shot" role="img" aria-label="Product photo of colourful foam shape blocks"><span style="background:linear-gradient(90deg,#e05a3a,#f2c94c,#3a8fd0)"></span></div><p>Lorem ipsum dolor sit amet, consectetur adipiscing elit. Aliquam rhoncus nulla sapien, tincidunt iaculis erat feugiat et.</p></div>
        <div class="product"><div class="shot" role="img" aria-label="Product photo of a black mini trampoline"><span style="background:#2b2f33"></span></div><p>Lorem ipsum dolor sit amet, consectetur adipiscing elit. Aliquam rhoncus nulla sapien, tincidunt iaculis erat feugiat et.</p></div>
        <div class="product"><div class="shot" role="img" aria-label="Product photo of a red springboard"><span style="background:linear-gradient(#d8332f,#d8b27a)"></span></div><p>Lorem ipsum dolor sit amet, consectetur adipiscing elit. Aliquam rhoncus nulla sapien, tincidunt iaculis erat feugiat et.</p></div>
        <div class="product"><div class="shot" role="img" aria-label="Product photo of a wooden balance stand"><span style="background:#c9a26a;width:14px"></span></div><p>Lorem ipsum dolor sit amet, consectetur adipiscing elit. Aliquam rhoncus nulla sapien, tincidunt iaculis erat feugiat et.</p></div>
      </div>
      <div class="page-foot"><span class="site">www.website.com</span></div>
    </article>
  </section>

</main>
</body>
</html>
```